Stationery Design Refresh - Velmora

We are Velmora - a small training & consulting company in Australia.
We HAVE a logo, but want to tweak it (original eps files available).

We want to the following outputs:
Change our stylised 'G' and possibly the current colour scheme is blue & green - we think that does not work very well.

Once that is done, we need to translate that into a PPT master and a letterhead. (Examples of current provided.)

We need a banner (for our website) and a few treatments of the icons used in the design (explained below)

The design 'language ' we want to adopt is:
Conversation bubbles
Grafitti
Hand painting

The 'g' should be stylised as two conversation bubbles.
We want to use these bubbles - and several different ones - as a feature in PPT presentations and therefore need a PPT Master

We need the banner to reflect the above.

The banner will be used as a website header and also as a 'strip' across the bottom of the letterhead.

With the above we are trying to communicate:
Handwritten/ Involved/ Authentic
Passionate & Playful (but NOT cartoonish)
Smart/ Creative/Innovative

Target Market(s)

B2B (employees and managers)

Industry/Entity Type

Training

Requirements
Should not have
• We use blue and green at the moment. But willing to change that or use it differently. I don't want the design to be cartoons and not overly colourful - we still need a corporate feel.

```html
<!DOCTYPE html>
<html lang="en">
<head>
<meta charset="utf-8">
<title>Velmora Letterhead</title>
<link href="https://fonts.googleapis.com/css2?family=Carlito:wght@400;700&display=swap" rel="stylesheet">
<style>
  :root {
    --backdrop: #2e2e2e;
    --paper: #ffffff;
    --ink: #1a1a1a;
    --muted: #6b6b6b;
    --brand-blue: #0f7ab4;
    --brand-black: #111111;
  }
  html, body {
    margin: 0;
    padding: 0;
    width: 1200px;
    height: 900px;
    overflow: hidden;
    background: var(--backdrop);
    font-family: "Carlito", "Calibri", sans-serif;
  }
  .letterhead {
    position: absolute;
    left: 320px;
    top: 53px;
    width: 560px;
    height: 793px;
    background: var(--paper);
  }
  .header-mark {
    position: absolute;
    right: 47px;
    top: 44px;
    display: flex;
    flex-direction: column;
    align-items: flex-end;
    gap: 5px;
  }
  .header-mark .dot {
    width: 30px;
    height: 30px;
    border-radius: 50%;
    background: var(--brand-blue);
  }
  .header-mark .name {
    font-size: 17px;
    font-weight: 700;
    color: var(--brand-black);
    line-height: 1;
  }
  .letter-body {
    position: absolute;
    left: 94px;
    top: 160px;
    font-size: 10.2px;
    line-height: 12.1px;
    color: var(--ink);
    white-space: nowrap;
  }
  .letter-body p {
    margin: 0 0 12.1px 0;
  }
  .letter-body .line {
    display: block;
  }
  .letter-footer {
    position: absolute;
    left: 0;
    right: 0;
    top: 727px;
  }
  .contact {
    position: absolute;
    left: 137px;
    width: 280px;
    text-align: center;
    font-size: 6.6px;
    line-height: 10px;
    color: var(--muted);
    white-space: nowrap;
  }
  .footer-mark {
    position: absolute;
    left: 437px;
    top: -4px;
    display: flex;
    align-items: center;
    gap: 4px;
  }
  .footer-mark .dot {
    width: 10px;
    height: 10px;
    border-radius: 50%;
    background: var(--brand-blue);
  }
  .footer-mark .name {
    font-size: 19px;
    font-weight: 700;
    color: var(--brand-black);
    line-height: 1;
  }
</style>
</head>
<body>
  <main class="letterhead">
    <div class="header-mark">
      <span class="dot"></span>
      <span class="name">Velmora</span>
    </div>

    <section class="letter-body">
      <p>Dear</p>
      <p>
        <span class="line">Lorem ipsum dolor sit amet, consectetur adipiscing elit. Vivamus gravida diam sit amet</span>
        <span class="line">arcu condimentum fermentum. Ut et sagittis nisl. Proin tincidunt pulvinar diam eu</span>
        <span class="line">adipiscing. Aenean nisl ipsum, mattis eget pellentesque nec, imperdiet a justo. Ut quis</span>
        <span class="line">mauris velit, id placerat nisi. Nullam suscipit tristique ante. Aliquam lacus nunc, varius</span>
        <span class="line">ac accumsan at, semper at sapien. Suspendisse metus mi, laoreet sed lacinia in,</span>
        <span class="line">fermentum vehicula orci. Lorem ipsum dolor sit amet, consectetur adipiscing elit.</span>
        <span class="line">Quisque fringilla sodales vulputate. Duis sodales ante quis metus laoreet vehicula. Cras</span>
        <span class="line">hendrerit nunc eu quam dignissim tincidunt. Mauris congue sem vitae ligula varius at</span>
        <span class="line">laoreet eros lobortis.</span>
      </p>
      <p>
        <span class="line">Maecenas ac arcu eu risus luctus commodo et non neque. Mauris vitae dui vitae leo</span>
        <span class="line">iaculis tincidunt. Quisque blandit, urna in dignissim interdum, urna augue lobortis</span>
        <span class="line">justo, sit amet eleifend ipsum arcu vitae nulla. In augue mauris, auctor quis malesuada</span>
        <span class="line">eget, aliquet ut nunc. Integer vitae erat mauris. Donec at felis quam. Nullam id sem mi,</span>
        <span class="line">quis varius sem. Sed tortor lorem, fermentum id condimentum nec, viverra vitae mi. Ut</span>
        <span class="line">augue sapien, varius ac convallis mattis, eleifend ut purus. In massa leo, vestibulum</span>
        <span class="line">nec molestie nec, adipiscing vel purus. Vivamus non laoreet mi. Fusce tempor porta</span>
        <span class="line">venenatis. Quisque tempor libero vel libero porta hendrerit volutpat libero rutrum.</span>
        <span class="line">Fusce sit amet lacus lectus.</span>
      </p>
      <p>
        <span class="line">Curabitur et felis vel ante auctor fermentum. In scelerisque faucibus hendrerit. Cura-</span>
        <span class="line">bitur interdum interdum nisi, at viverra ligula ultricies posuere. Suspendisse potenti.</span>
        <span class="line">Maecenas aliquet, leo eget mattis sollicitudin, magna mauris eleifend lectus, sit amet</span>
        <span class="line">eleifend eros enim at orci. Duis purus tortor, lobortis vel adipiscing sed, fringilla</span>
        <span class="line">dapibus enim. Duis id turpis augue, non feugiat lorem. Integer et ullamcorper ligula.</span>
        <span class="line">Nulla et elit nisi, et molestie mauris. Nam gravida nulla.</span>
      </p>
      <p>
        <span class="line">id justo aliquet vitae pellentesque nibh tincidunt. Vestibulum scelerisque diam sit amet</span>
        <span class="line">mauris posuere scelerisque. Vivamus eu enim sit amet felis pretium vestibulum.</span>
        <span class="line">Pellentesque ut tellus ac purus fringilla tristique. Donec nec condimentum justo.</span>
      </p>
    </section>

    <footer class="letter-footer">
      <div class="contact">
        PO Box 418 Tarrawong NSW 2590 &nbsp;/&nbsp; Phone: +61-2-4100 5293 &nbsp;/&nbsp; Fax: +61-2-8100 3318<br>
        www.velmora.com.au
      </div>
      <div class="footer-mark">
        <span class="dot"></span>
        <span class="name">Velmora</span>
      </div>
    </footer>
  </main>
</body>
</html>
```